VERUNDA

It’s is a startup business. We design and build new products.

Target Market(s)

For my first two products, they are targeting the laundry market, hanger accessory, and new modern style clothes dryer. I also have a Pet Treat product at patent stage, and there are other products not yet started but will be more engineering based. Therefore from young adults to older population

Industry/Entity Type

Colours of website to match the logo (att)

Coding

Coded - Design and coding required

Number of Pages Required

1 page

Font styles to use
Other font styles liked:
• Some of the same font as the logo

Colors

Designer to choose colors to be used in the design.

Requirements
Must have
• An upbeat vibe - the logo looks great so inline with that !
Should not have
• anything old fashioned and old style fonts

```html
<!DOCTYPE html>
<html lang="en">
<head>
<meta charset="utf-8">
<title>Verunda – Innovative Products for Your Everyday Life</title>
<link rel="stylesheet" href="https://fonts.googleapis.com/css2?family=Michroma&family=Montserrat:wght@400;500;600;700;800&display=swap">
<style>
:root{
  --navy:#0b1d3a;
  --navy-deep:#06122a;
  --indigo:#28237a;
  --royal:#2f45b8;
  --teal:#17c3cf;
  --teal-dark:#0a9fb4;
  --cyan:#22b8e6;
  --ink:#1c2333;
  --muted:#5a6272;
  --white:#ffffff;
  --soft:#eef8fb;
}
*{box-sizing:border-box;margin:0;padding:0}
html,body{width:1200px;height:3180px;overflow:hidden}
body{font-family:"Montserrat",sans-serif;color:var(--ink);background:var(--white);position:relative}
.display{font-family:"Michroma",sans-serif;letter-spacing:.12em}

/* Header */
.site-header{position:absolute;top:0;left:0;width:1200px;height:200px;z-index:5}
.brand{position:absolute;left:70px;top:56px;display:flex;align-items:center;gap:16px;
  font-family:"Montserrat",sans-serif;font-weight:800;font-size:40px;color:var(--white);letter-spacing:.06em}
.brand-dot{width:30px;height:30px;border-radius:50%;background:var(--teal)}
.top-bar{position:absolute;right:0;top:0;width:560px;height:86px;background:var(--white);
  display:flex;align-items:center;padding-left:110px;gap:18px}
.social{width:34px;height:34px;border-radius:50%;background:var(--navy)}
.call{margin-left:30px;display:flex;align-items:center;gap:10px}
.call-icon{width:38px;height:38px;border-radius:50%;background:var(--teal);display:flex;align-items:center;justify-content:center}
.call small{display:block;font-size:11px;color:var(--muted);font-weight:600}
.call strong{font-size:19px;color:var(--ink);font-weight:700}
.main-nav{position:absolute;right:0;top:86px;width:640px;height:52px;background:var(--teal);
  display:flex;align-items:center;justify-content:space-around;padding:0 24px}
.main-nav a{color:var(--white);text-decoration:none;font-size:15px;font-weight:700;letter-spacing:.04em}
.main-nav a.active{border-bottom:2px solid var(--white);padding-bottom:4px}

/* Hero */
.hero{position:absolute;top:0;left:0;width:1200px;height:800px;
  clip-path:polygon(0 0,100% 0,100% 78%,50% 100%,0 86%);
  background:radial-gradient(circle at 75% 35%,#4f7fd0 0%,#1c3c80 22%,#0c1f4a 48%,#050d24 80%)}
.hero-visual{position:absolute;right:0;top:140px;width:620px;height:460px;
  background:radial-gradient(ellipse at 55% 45%,rgba(180,210,255,.55) 0%,rgba(80,130,220,.25) 40%,rgba(0,0,0,0) 70%)}
.hero-copy{position:absolute;left:70px;top:290px;color:var(--white)}
.hero-copy h1{font-size:50px;line-height:1.12;font-weight:800;letter-spacing:.01em}
.hero-copy p{margin-top:18px;font-size:19px;font-weight:500}
.hero-actions{margin-top:34px;display:flex;gap:22px}
.btn{display:inline-block;padding:14px 30px;border-radius:30px;font-size:16px;font-weight:700;color:var(--white);text-decoration:none}
.btn-teal{background:var(--teal)}
.btn-outline{background:var(--teal-dark);border:2px solid var(--teal)}
.btn-navy{background:var(--indigo)}
.hero-edge{position:absolute;left:0;top:560px;width:1200px;height:260px;z-index:2}

/* About */
.about{position:absolute;top:800px;left:0;width:1200px;height:520px}
.about-visual{position:absolute;left:120px;top:50px;width:400px;height:440px;
  background:linear-gradient(150deg,#1bd0d0 0%,#1f8fd6 45%,#262f8f 100%);
  clip-path:polygon(20% 0,100% 12%,80% 100%,0 80%)}
.about-copy{position:absolute;left:640px;top:80px;width:520px}
.eyebrow{color:var(--teal);font-size:17px;font-weight:700;letter-spacing:.04em}
.section-title{font-family:"Michroma",sans-serif;font-size:34px;letter-spacing:.2em;color:var(--ink);margin-top:6px}
.about-copy h3{margin-top:26px;font-size:18px;font-weight:700;line-height:1.4}
.about-copy p{margin-top:14px;font-size:15px;line-height:1.65;color:var(--muted)}
.about-copy .btn{margin-top:26px}

/* Panels */
.panels{position:absolute;top:1320px;left:0;width:1200px;height:740px}
.panel{position:absolute;top:0;height:740px;width:640px;color:var(--white);text-align:center}
.panel-laundry{left:0;background:linear-gradient(160deg,#3a4fc8 0%,#2a2e8c 60%,#1d1f6a 100%);
  clip-path:polygon(0 4%,100% 15%,94% 100%,0 92%)}
.panel-pet{right:0;background:linear-gradient(200deg,#1fc7e8 0%,#1a9fd8 60%,#1677c0 100%);
  clip-path:polygon(6% 15%,100% 4%,100% 92%,0 100%)}
.panel-inner{position:absolute;top:170px;width:460px}
.panel-laundry .panel-inner{left:80px}
.panel-pet .panel-inner{left:120px}
.panel-icon{width:110px;height:100px;margin:0 auto;border-radius:10px;background:rgba(255,255,255,.22)}
.panel h2{font-family:"Michroma",sans-serif;font-size:25px;letter-spacing:.18em;margin-top:26px;font-weight:400}
.panel-rule{width:50px;height:3px;background:var(--white);margin:16px auto}
.panel p{font-size:15px;line-height:1.6;padding:0 20px}
.panel .btn{margin-top:24px}

/* Why choose */
.why{position:absolute;top:2100px;left:0;width:1200px;height:520px;text-align:center}
.why .eyebrow{font-size:19px}
.why .section-title{font-size:30px}
.cards{position:absolute;top:130px;left:100px;width:1000px;display:flex;gap:24px}
.card{width:232px;height:290px;background:var(--white);border-radius:18px;text-align:left;padding:28px 24px;
  box-shadow:0 10px 30px rgba(20,60,90,.12)}
.card.featured{border:2px solid var(--teal);background:var(--soft);transform:translateY(-12px)}
.card-icon{width:58px;height:58px;border-radius:50%;background:var(--teal);display:flex;align-items:center;justify-content:center}
.card h4{margin-top:22px;font-size:17px;font-weight:800}
.card p{margin-top:12px;font-size:14px;line-height:1.6;color:var(--muted)}
.why .btn{position:absolute;top:440px;left:520px}

/* Footer */
.site-footer{position:absolute;top:2600px;left:0;width:1200px;height:580px;color:var(--white)}
.footer-bg{position:absolute;inset:0}
.footer-brand{position:absolute;top:130px;left:0;width:1200px;display:flex;justify-content:center;align-items:center;gap:18px;
  font-size:64px;font-weight:800;letter-spacing:.06em}
.footer-brand .brand-dot{width:44px;height:44px}
.footer-cols{position:absolute;top:360px;left:100px;width:1020px;display:flex;gap:60px}
.footer-cols h5{font-size:21px;font-weight:800;letter-spacing:.04em;margin-bottom:22px}
.col-links{width:260px}
.col-contact{width:360px}
.col-sub{width:400px}
.footer-cols ul{list-style:none}
.footer-cols li{font-size:15px;margin-bottom:14px;display:flex;align-items:center;gap:12px}
.subscribe{display:flex;margin-top:6px}
.subscribe span{flex:1;height:46px;background:var(--white);border-radius:24px 0 0 24px;color:#8a92a0;font-size:14px;padding:14px 22px}
.subscribe b{background:var(--teal);border-radius:24px;margin-left:-20px;padding:14px 30px;font-size:15px}
.copyright{position:absolute;bottom:14px;left:0;width:1200px;text-align:center;font-size:13px;color:#aab4c4}
</style>
</head>
<body>

<section class="hero">
  <div class="hero-visual" role="img" aria-label="Photo of a hand touching a glowing digital interface"></div>
  <div class="hero-copy">
    <h1>INNOVATIVE PRODUCTS<br>FOR YOUR EVERYDAY<br>LIFE</h1>
    <p>Designing smarter solutions for laundry, pets, &amp; beyond.</p>
    <div class="hero-actions">
      <a class="btn btn-teal" href="#">See What's New</a>
      <a class="btn btn-outline" href="#">Explore Our Products</a>
    </div>
  </div>
</section>
<svg class="hero-edge" viewBox="0 0 1200 260" aria-hidden="true">
  <polygon points="0,128 600,240 1200,76 1200,92 600,258 0,146" fill="#17c3cf"/>
</svg>

<header class="site-header">
  <div class="brand"><span class="brand-dot"></span>VERUNDA</div>
  <div class="top-bar">
    <span class="social"></span><span class="social"></span><span class="social"></span>
    <div class="call">
      <span class="call-icon"><svg width="18" height="18" viewBox="0 0 24 24"><path d="M6.6 10.8a15 15 0 0 0 6.6 6.6l2.2-2.2a1 1 0 0 1 1-.25 11 11 0 0 0 3.6.6 1 1 0 0 1 1 1V20a1 1 0 0 1-1 1A17 17 0 0 1 3 4a1 1 0 0 1 1-1h3.5a1 1 0 0 1 1 1c0 1.25.2 2.45.6 3.6a1 1 0 0 1-.25 1z" fill="#fff"/></svg></span>
      <div><small>CALL US</small><strong>+1 555 014 (2290)</strong></div>
    </div>
  </div>
  <nav class="main-nav">
    <a class="active" href="#">HOME</a><a href="#">ABOUT US</a><a href="#">INNOVATIONS</a><a href="#">PRODUCTS</a><a href="#">CONTACT US</a>
  </nav>
</header>

<section class="about">
  <div class="about-visual" role="img" aria-label="Large three-dimensional brand emblem in teal and indigo"></div>
  <div class="about-copy">
    <div class="eyebrow">WHO WE ARE</div>
    <h2 class="section-title">ABOUT US</h2>
    <h3>Innovating Everyday Essentials – Smart Design,<br>Smart Living.</h3>
    <p>At Verunda, we believe that the best products are those that seamlessly blend functionality, modern aesthetics, and intelligent design. We are a product innovation company dedicated to reimagining the everyday – from laundry accessories to pet care solutions and beyond!</p>
    <p>To design and build smart products that simplify daily life, offering practical solutions with engineering precision and contemporary style.</p>
    <a class="btn btn-teal" href="#">Learn More</a>
  </div>
</section>

<section class="panels">
  <div class="panel panel-laundry">
    <div class="panel-inner">
      <div class="panel-icon" role="img" aria-label="Laundry machine icon"></div>
      <h2>LAUNDRY SOLUTIONS</h2>
      <div class="panel-rule"></div>
      <p>A sleek, efficient, and space-saving drying solution. This next-generation clothes dryer is designed for modern homes, combining style with smart drying technology.</p>
      <a class="btn btn-teal" href="#">Learn More</a>
    </div>
  </div>
  <div class="panel panel-pet">
    <div class="panel-inner">
      <div class="panel-icon" role="img" aria-label="Pet care icon"></div>
      <h2>PET INNOVATIONS</h2>
      <div class="panel-rule"></div>
      <p>A game-changing treat innovation is on the way! Currently in the patent stage, this product is designed to provide healthier, more convenient treat options for pets.</p>
      <a class="btn btn-navy" href="#">Learn More</a>
    </div>
  </div>
</section>

<section class="why">
  <div class="eyebrow">OUR PRODUCTS ARE DESIGNED TO MAKE YOUR LIFE EASIER</div>
  <h2 class="section-title">WHY CHOOSE US?</h2>
  <div class="cards">
    <article class="card">
      <div class="card-icon"><svg width="28" height="28" viewBox="0 0 24 24"><path d="M4 4h6v2H6v4H4zM20 4v6h-2V6h-4V4zM4 20v-6h2v4h4v2zM20 20h-6v-2h4v-4h2z" fill="#fff"/></svg></div>
      <h4>SPACE-SAVING</h4>
      <p>Compact forms that fold away and free up room at home.</p>
    </article>
    <article class="card featured">
      <div class="card-icon"><svg width="28" height="28" viewBox="0 0 24 24"><path d="M13 2 4 14h7l-1 8 9-12h-7z" fill="#fff"/></svg></div>
      <h4>ENERGY-EFFICIENT</h4>
      <p>Low power use that keeps running costs down every single day.</p>
    </article>
    <article class="card">
      <div class="card-icon"><svg width="28" height="28" viewBox="0 0 24 24"><path d="M12 2 4 5v6c0 5 3.4 9.4 8 11 4.6-1.6 8-6 8-11V5z" fill="#fff"/></svg></div>
      <h4>DURABLE</h4>
      <p>Built from tough parts made to last through daily heavy use.</p>
    </article>
    <article class="card">
      <div class="card-icon"><svg width="28" height="28" viewBox="0 0 24 24"><path d="M20 4C10 4 4 9 4 16c0 1.5.4 2.8 1 4 1-4 4-7 9-9-4 3-6 6-7 10 1 .6 2.3 1 4 1 7 0 9-8 9-18z" fill="#fff"/></svg></div>
      <h4>ECO-FRIENDLY</h4>
      <p>Recyclable materials chosen to reduce waste across the lifecycle.</p>
    </article>
  </div>
  <a class="btn btn-navy" href="#">Explore More</a>
</section>

<footer class="site-footer">
  <svg class="footer-bg" viewBox="0 0 1200 580" preserveAspectRatio="none" aria-hidden="true">
    <polygon points="0,110 600,20 1200,70 1200,580 0,580" fill="#142033"/>
    <polygon points="0,60 600,0 1200,40 1200,70 600,20 0,110" fill="#17c3cf"/>
    <polygon points="0,110 600,20 620,24 0,130" fill="#0a9fb4"/>
  </svg>
  <div class="footer-brand"><span class="brand-dot"></span>VERUNDA</div>
  <div class="footer-cols">
    <div class="col-links">
      <h5>QUICK LINKS</h5>
      <ul>
        <li>› Home</li><li>› About Us</li><li>› Our Innovations</li><li>› Why Choose Us?</li><li>› Contact Us</li>
      </ul>
    </div>
    <div class="col-contact">
      <h5>CONTACT US</h5>
      <ul>
        <li><svg width="16" height="16" viewBox="0 0 24 24"><path d="M12 2a7 7 0 0 0-7 7c0 5 7 13 7 13s7-8 7-13a7 7 0 0 0-7-7zm0 9.5A2.5 2.5 0 1 1 12 6.5a2.5 2.5 0 0 1 0 5z" fill="#17c3cf"/></svg>14 Harbor Lane, Suite 3, 560218</li>
        <li><svg width="16" height="16" viewBox="0 0 24 24"><path d="M6.6 10.8a15 15 0 0 0 6.6 6.6l2.2-2.2a1 1 0 0 1 1-.25 11 11 0 0 0 3.6.6 1 1 0 0 1 1 1V20a1 1 0 0 1-1 1A17 17 0 0 1 3 4a1 1 0 0 1 1-1h3.5a1 1 0 0 1 1 1c0 1.25.2 2.45.6 3.6a1 1 0 0 1-.25 1z" fill="#17c3cf"/></svg>+1 555 014 (2290)</li>
        <li><svg width="16" height="16" viewBox="0 0 24 24"><path d="M3 5h18v14H3zm2 2v.5l7 4.5 7-4.5V7z" fill="#17c3cf"/></svg>hello@verunda-demo.com</li>
        <li><svg width="16" height="16" viewBox="0 0 24 24"><circle cx="12" cy="12" r="9" fill="none" stroke="#17c3cf" stroke-width="2"/><path d="M3 12h18M12 3c3 3 3 15 0 18M12 3c-3 3-3 15 0 18" fill="none" stroke="#17c3cf" stroke-width="1.6"/></svg>www.verunda-demo.com</li>
      </ul>
    </div>
    <div class="col-sub">
      <h5>SUBSCRIBE FOR UPDATES</h5>
      <div class="subscribe"><span>Email Address</span><b>Subscribe</b></div>
    </div>
  </div>
  <div class="copyright">(C) Copyright | All Rights Reserved</div>
</footer>

</body>
</html>
```